VNT's Blade spring flyers

I am needing a flyer design for my lawn mowing business. my services are mowing, edging, weed eating, vacuuming with strong attention to detail. residential and commercial. Mowing average $35 and Spring clean up average $79. Looking for fun, professional and colorful to grab the eye and stand out. rough sizing of 10"x4"

Target Market(s)

people needing lawn care and spring clean up

Font styles to use
Serif

Colors

Designer to choose colors to be used in the design.

Requirements
Must have
• Services listed and pricing listed
• please add licensed and insured
• 555-318-4402
• brokaweston5@fernpost.example
• FREE ESTIMATES

```html
<!DOCTYPE html>
<html lang="en">
<head>
<meta charset="utf-8">
<title>VNT's Blade Lawn Care – Spring Flyer</title>
<link rel="stylesheet" href="https://fonts.googleapis.com/css2?family=Montserrat:wght@700;800&family=Roboto:ital,wght@0,500;1,500;1,700&display=swap">
<style>
  :root {
    --page-bg: #1586c8;
    --paper: #f1f1f1;
    --brand-blue: #1670b8;
    --charcoal: #323334;
    --ink: #111111;
    --turf-dark: #1f4a1f;
    --turf-mid: #2f6a2a;
    --grass-light: #7cc447;
    --grass-dark: #2f7a22;
    --white: #ffffff;
  }
  * { box-sizing: border-box; margin: 0; padding: 0; }
  html, body { width: 1144px; height: 1200px; overflow: hidden; }
  body { background: var(--page-bg); position: relative; font-family: "Roboto", sans-serif; }

  .flyer {
    position: absolute; left: 350px; top: 37px;
    width: 444px; height: 1126px;
    background: var(--paper);
    overflow: hidden;
  }

  /* Header */
  .business-name {
    position: absolute; top: 172px; left: 0; width: 100%;
    text-align: center;
    font-family: "Roboto", sans-serif; font-weight: 500;
    font-size: 30px; line-height: 1; color: var(--charcoal);
  }
  .licensed {
    position: absolute; top: 227px; left: 64px; width: 318px; height: 27px;
    background: var(--charcoal); color: var(--white);
    font-style: italic; font-weight: 500; font-size: 18px;
    display: flex; align-items: center; justify-content: center;
  }

  /* Services band */
  .turf {
    position: absolute; top: 306px; left: 0; width: 100%; height: 334px;
    background: radial-gradient(ellipse at 50% 40%, var(--turf-mid), var(--turf-dark));
  }
  .services { position: absolute; top: 360px; left: 69px; list-style: none; }
  .service {
    display: flex; align-items: center; gap: 18px; height: 59.5px;
    font-family: "Montserrat", sans-serif; font-weight: 800; font-size: 28px;
    color: var(--white);
  }
  .service-num {
    width: 42px; height: 42px; border-radius: 50%;
    background: var(--white); color: var(--charcoal);
    display: flex; align-items: center; justify-content: center;
    font-family: "Roboto", sans-serif; font-weight: 500; font-size: 30px;
  }

  /* Details */
  .details { position: absolute; top: 685px; left: 0; width: 100%; text-align: center; }
  .tagline { font-style: italic; font-weight: 700; font-size: 15.5px; line-height: 21px; color: var(--ink); }
  .pricing {
    margin: 17px auto 0; width: 314px; height: 59px; border-radius: 30px;
    background: var(--brand-blue); color: var(--white);
    font-weight: 500; font-size: 16px; line-height: 22px;
    display: flex; align-items: center; justify-content: center;
  }
  .contact { margin-top: 20px; font-style: italic; font-weight: 700; font-size: 15px; line-height: 21px; color: var(--ink); }

  /* Footer grass */
  .grass {
    position: absolute; left: 0; bottom: 0; width: 100%; height: 240px;
    background: linear-gradient(to bottom, rgba(124,196,71,0) 0%, var(--grass-light) 25%, var(--grass-dark) 100%);
  }
  .estimates {
    position: absolute; top: 1015px; left: 60px; width: 326px; height: 55px;
    border-radius: 28px; background: var(--brand-blue); color: var(--white);
    font-family: "Montserrat", sans-serif; font-weight: 700; font-size: 30px;
    display: flex; align-items: center; justify-content: center;
  }
</style>
</head>
<body>
  <main class="flyer">
    <header>
      <h1 class="business-name">VNT's Blade Lawn Care</h1>
    </header>
    <div class="licensed">Licensed And Insured</div>

    <div class="turf" role="img" aria-label="Close-up of green lawn turf"></div>
    <ol class="services">
      <li class="service"><span class="service-num">1</span>MOWING</li>
      <li class="service"><span class="service-num">2</span>EDGING</li>
      <li class="service"><span class="service-num">3</span>WEED REMOVING</li>
      <li class="service"><span class="service-num">4</span>VACUUMING</li>
    </ol>

    <section class="details">
      <p class="tagline">STRONG ATTENTION TO DETAIL<br>RESIDENTIAL AND COMMERCIAL</p>
      <p class="pricing">MOWING AVERAGE $35 &amp;<br>SPRING CLEAN UP AVERAGE $79</p>
      <p class="contact">555-318-4402<br>BROKAWESTON5@FERNPOST.EXAMPLE</p>
    </section>

    <div class="grass" role="img" aria-label="Tall fresh green grass blades"></div>
    <div class="estimates">FREE ESTIMATES</div>
  </main>
</body>
</html>
```